New Hotel Showcase Website

We plan to launch a website called www.fernlodgings.net which showcases the world’s best new hotels. We want a mock up for 2 pages: the homepage (page 1) and the individual hotel page (page 2). We are looking for a design which combines simplicity while highlighting images/features of the hotel. Because the theme of the site is new hotels it is important that the design somehow emphasizes the age of each hotel listed – both on the homepage and then on the individual hotel page.

NOTE: WE WANT A CREATIVE, NEW APPROACH TO DISPLAYING HOTELS. NOT JUST A COPY OF CURRENT HOTEL WEBSITES.

The design should consider unique and creative ways of helping users to navigate the homepage (page 1) based on the age, location or style of the hotel they are interested in. The individual hotel page(page 2) can be more standard by clearly setting out hotel photos, feature lists, reviews, contact details and potential discounts. There is no booking system needed as this is not a hotel booking website.

The design should ideally be compatible with a content management system such as Page Forge. In terms of reference materials we like sites similar to:

http://www.quillwanderer.net
http://www.bobandkayporter.net
http://www.craftinns.net
http://www.pebblestays.net

These sites are designed far more simply than large booking sites such as www.voyaro.net, www.roomsy.net or even jaunt ledger. However, we are not looking for a copy of the above. We are looking for a design that presents hotels in a novel way and would be seen by the industry as a unique way of displaying new hotels.
Updates

Dear Designers - we have received quite a few entries already. Thank you. However, none of the designs submitted have responded to our brief. They are all copies or derivatives of current hotel websites which is not what we are looking for. We want (a) a new and creative approach to a hotel website and (b) one which creatively uses the age of the hotel (ie. 1 month old, 6 months old etc).

It will require creative thinking and new ideas. We wanted to challenge designers to come up with something new. Thanks.

```html
<!DOCTYPE html>
<html lang="en">
<head>
<meta charset="utf-8">
<title>Fern Lodgings – The Regency Park</title>
<link rel="stylesheet" href="https://fonts.googleapis.com/css2?family=Figtree:wght@400;600;700&display=swap">
<style>
  :root {
    --ink: #5a6178;
    --ink-soft: #a3a8b8;
    --green: #9cc43a;
    --orange: #ef922f;
    --band: #d4d8e3;
    --top-band: #e4e5e9;
    --panel: #f0f1f3;
    --rule: #d3d5db;
    --slate: #6a7186;
    --empty-dot: #e6e7eb;
  }
  * { box-sizing: border-box; margin: 0; padding: 0; }
  html, body { width: 1200px; height: 1000px; overflow: hidden; background: #fff; }
  body { font-family: "Figtree", sans-serif; color: var(--ink); position: relative; }

  .masthead { position: absolute; left: 0; top: 0; width: 1200px; height: 215px; }

  .feature { position: absolute; left: 440px; top: 240px; width: 320px; height: 100px;
    border-left: 1px solid #c9ccd6; border-right: 1px solid #c9ccd6; text-align: center; }
  .feature__name { font-size: 28px; font-weight: 700; line-height: 26px; letter-spacing: -0.2px; }
  .feature__place { font-size: 16px; margin-top: 4px; line-height: 20px; }
  .feature__opened { font-size: 16px; color: var(--ink-soft); margin-top: 5px; line-height: 20px; }
  .age-meter { position: absolute; left: 42px; top: 84px; }

  .feature__intro { position: absolute; left: 200px; top: 364px; width: 800px; text-align: center;
    font-size: 16px; line-height: 25px; letter-spacing: -0.15px; white-space: nowrap; }

  .btn { display: inline-flex; align-items: center; gap: 9px; background: var(--green); color: #fff;
    font-weight: 600; text-decoration: none; }
  .btn::after { content: ""; border-left: 5px solid #fff; border-top: 5px solid transparent; border-bottom: 5px solid transparent; }
  .btn--large { position: absolute; left: 530px; top: 454px; width: 140px; height: 36px; font-size: 16px; padding-left: 13px; }
  .btn--small { height: 30px; font-size: 16px; padding: 0 9px; margin-top: 14px; letter-spacing: -0.2px; }

  .panel { position: absolute; top: 550px; width: 460px; height: 202px; }
  .panel--latest { left: 120px; border-top: 2px solid var(--orange); }
  .panel--suggest { left: 620px; border-top: 2px solid var(--green); }
  .panel__title { height: 48px; padding-left: 19px; font-size: 24px; font-weight: 400; line-height: 46px;
    border-bottom: 1px solid var(--rule); }
  .panel--suggest .panel__title { padding-left: 21px; }
  .panel__body { background: var(--panel); height: 152px; position: relative; padding: 17px 19px 0; overflow: hidden; }

  .hotel-list { display: flex; }
  .hotel-card { width: 230px; }
  .hotel-card + .hotel-card { border-left: 1px solid #c9ccd6; padding-left: 18px; }
  .hotel-card__name { font-size: 18px; font-weight: 700; line-height: 20px; }
  .hotel-card__place { font-size: 16px; margin-top: 5px; line-height: 20px; }
  .hotel-card .btn { margin-left: 1px; }
  .view-all { position: absolute; left: 19px; top: 116px; color: var(--green); font-size: 16px; text-decoration: none; }

  .suggest__text { font-size: 15px; line-height: 25px; letter-spacing: -0.2px; white-space: nowrap; }
  .suggest-form { display: flex; align-items: flex-end; margin-top: 12px; }
  .field { display: flex; flex-direction: column; margin-right: 10px; }
  .field label { font-size: 16px; line-height: 20px; margin-bottom: 6px; }
  .field input { width: 170px; height: 24px; border: 1px solid #c5c8d0; background: #fff; margin-left: 1px; }
  .btn-send { width: 60px; height: 24px; background: var(--slate); color: #fff; border: 0; font-family: inherit;
    font-weight: 600; font-size: 14px; }

  .site-footer { position: absolute; left: 120px; top: 799px; width: 960px; height: 61px;
    border-top: 1px solid var(--rule); border-bottom: 1px solid var(--rule); display: flex; align-items: center; }
  .footer-nav { display: flex; }
  .footer-nav a { color: var(--green); font-size: 14px; text-decoration: none; letter-spacing: -0.1px; }
  .newsletter { margin-left: auto; display: flex; align-items: center; }
  .newsletter__label { font-size: 18px; margin-right: 15px; }
  .newsletter input { width: 200px; height: 24px; border: 1px solid #c5c8d0; padding-left: 7px; font-family: inherit;
    font-size: 14px; color: var(--ink); margin-right: 10px; }
  .newsletter input::placeholder { color: var(--ink); }
  .btn-signup { width: 90px; height: 24px; background: var(--green); color: #fff; border: 0; font-family: inherit; font-weight: 600; font-size: 14px; }

  .legal { position: absolute; left: 100px; top: 884px; width: 1000px; text-align: center; font-size: 13px; line-height: 20px;
    letter-spacing: -0.2px; white-space: nowrap; }
  .copyright { position: absolute; left: 0; top: 937px; width: 1200px; text-align: center; font-size: 11px; }
</style>
</head>
<body>

<svg class="masthead" viewBox="0 0 1200 215">
  <defs>
    <linearGradient id="lobby" x1="0" y1="0" x2="1" y2="1">
      <stop offset="0" stop-color="#a89a86"/>
      <stop offset="0.35" stop-color="#7a5a44"/>
      <stop offset="0.6" stop-color="#9b6a4c"/>
      <stop offset="0.85" stop-color="#6e4a38"/>
      <stop offset="1" stop-color="#b8a58a"/>
    </linearGradient>
    <linearGradient id="shadeL" x1="1" y1="0" x2="0" y2="0">
      <stop offset="0" stop-color="#c9ccd4"/>
      <stop offset="1" stop-color="#ffffff" stop-opacity="0"/>
    </linearGradient>
    <linearGradient id="shadeR" x1="0" y1="0" x2="1" y2="0">
      <stop offset="0" stop-color="#c9ccd4"/>
      <stop offset="1" stop-color="#ffffff" stop-opacity="0"/>
    </linearGradient>
  </defs>
  <rect x="0" y="0" width="1200" height="50" fill="var(--top-band)"/>
  <path d="M120,50 L120,180 Q80,120 40,50 Z" fill="url(#shadeL)"/>
  <path d="M1080,50 L1080,180 Q1120,120 1160,50 Z" fill="url(#shadeR)"/>
  <path d="M120,157 Q600,175 1080,157 L1080,172 L600,207 L120,172 Z" fill="var(--band)"/>
  <path d="M120,0 H1080 V157 Q600,175 120,157 Z" fill="url(#lobby)" role="img" aria-label="Photograph of the hotel lobby with sofas, armchairs and a polished marble floor"/>
</svg>

<section class="feature">
  <h1 class="feature__name">The Regency Park</h1>
  <p class="feature__place">London . UK</p>
  <p class="feature__opened">Opened 21 March 2013</p>
  <svg class="age-meter" width="236" height="14" viewBox="0 0 236 14" role="img" aria-label="Hotel age: 6 and a half months">
    <g fill="var(--green)">
      <rect x="0" width="14" height="14"/><rect x="20" width="14" height="14"/><rect x="40" width="14" height="14"/>
      <rect x="60" width="14" height="14"/><rect x="80" width="14" height="14"/><rect x="100" width="14" height="14"/>
      <rect x="120" width="8" height="14"/>
    </g>
    <g fill="var(--empty-dot)">
      <rect x="128" width="6" height="14"/>
      <rect x="140" width="14" height="14"/><rect x="160" width="14" height="14"/><rect x="180" width="14" height="14"/>
      <rect x="200" width="14" height="14"/><rect x="220" width="14" height="14"/>
    </g>
  </svg>
</section>

<p class="feature__intro">Lorem ipsum dolor sit amet, consectetur adipisicing elit, sed do eiusmod tempor incididunt ut<br>labore et dolore magna aliqua. Ut enim ad minim veniam, quis nostrud exercitation ullamco<br>laboris nisi ut aliquip ex dolor sit amet tempor incididunt ut labore commodo consequat.</p>
<a class="btn btn--large" href="#">Find out more</a>

<section class="panel panel--latest">
  <h2 class="panel__title">Latest hotels added</h2>
  <div class="panel__body">
    <div class="hotel-list">
      <article class="hotel-card">
        <h3 class="hotel-card__name">Hotel Palmanova</h3>
        <p class="hotel-card__place">Milan . Italy</p>
        <a class="btn btn--small" href="#">Find out more</a>
      </article>
      <article class="hotel-card">
        <h3 class="hotel-card__name">The Harbour View</h3>
        <p class="hotel-card__place">Sidney . Australia</p>
        <a class="btn btn--small" href="#">Find out more</a>
      </article>
    </div>
    <a class="view-all" href="#">View all new hotels added</a>
  </div>
</section>

<section class="panel panel--suggest">
  <h2 class="panel__title">Suggest a hotel</h2>
  <div class="panel__body">
    <p class="suggest__text">Lorem ipsum dolor sit amet consectetur adipisicing elit, sed<br>do eiusmod tempor incididunt ut labore et dolore magna:</p>
    <form class="suggest-form">
      <div class="field"><label for="hotel-name">Name of Hotel</label><input id="hotel-name" type="text"></div>
      <div class="field"><label for="hotel-location">Location</label><input id="hotel-location" type="text"></div>
      <button class="btn-send" type="button">Send</button>
    </form>
  </div>
</section>

<footer class="site-footer">
  <nav class="footer-nav">
    <a href="#" style="margin-right:51px">Home</a>
    <a href="#" style="margin-right:53px">About Us</a>
    <a href="#" style="margin-right:51px">Hotels</a>
    <a href="#" style="margin-right:51px">FAQs</a>
    <a href="#">Contact Us</a>
  </nav>
  <form class="newsletter">
    <span class="newsletter__label">Newsletter</span>
    <input type="email" placeholder="Enter your email address">
    <button class="btn-signup" type="button">Sign me up</button>
  </form>
</footer>

<p class="legal">Any legal information in here ipsum dolor sit amet, consectetur adipisicing elit, sed do eiusmod tempor incididunt ut labore et dolore magna<br>aliqua enim ad minim veniam, quis nostrud exercitation ullamco laboris nisi ut aliquip.</p>
<p class="copyright">© Copyright Fern Lodgings . All rights reserved</p>

</body>
</html>
```